HPS business cards

(Generators . Lighting Towers . De-watering Pumps . Compressors) put under the logo please. my details are Owen Pritchard (Director) 0461527390 harbourpinesupply@postvale.net

```html
<!DOCTYPE html>
<html lang="en">
<head>
<meta charset="utf-8">
<title>HPS Business Cards</title>
<link href="https://fonts.googleapis.com/css2?family=Open+Sans:wght@400;600;700&display=swap" rel="stylesheet">
<style>
  :root {
    --page-bg: #e9e4dc;
    --card-dark: #221f20;
    --brand-orange: #e8a232;
    --text-light: #f1f1f1;
    --rule-grey: #8c8c8c;
  }
  * { margin: 0; padding: 0; box-sizing: border-box; }
  html, body {
    width: 1200px;
    height: 900px;
    overflow: hidden;
    background: var(--page-bg);
    font-family: "Open Sans", Arial, sans-serif;
  }
  .canvas {
    position: relative;
    width: 1200px;
    height: 900px;
  }
  .card {
    position: absolute;
    left: 280px;
    width: 640px;
    height: 366px;
    box-shadow: 0 14px 30px rgba(0,0,0,0.28);
  }
  .card-front { top: 48px; }
  .card-back { top: 484px; }
  .card-frame {
    position: absolute;
    inset: 0;
    width: 100%;
    height: 100%;
  }
  .brand {
    position: absolute;
    display: flex;
    align-items: center;
    gap: 12px;
  }
  .brand-square {
    width: 34px;
    height: 34px;
    border: 4px solid var(--brand-orange);
  }
  .brand-name {
    color: var(--brand-orange);
    font-weight: 700;
    font-size: 30px;
    letter-spacing: 0.5px;
    text-transform: uppercase;
    line-height: 1;
  }
  .card-front .brand {
    left: 0;
    right: 0;
    top: 128px;
    justify-content: center;
  }
  .front-rule {
    position: absolute;
    left: 90px;
    right: 90px;
    top: 196px;
    height: 1px;
    background: linear-gradient(90deg, transparent, var(--brand-orange), transparent);
  }
  .services {
    position: absolute;
    left: 0;
    right: 0;
    top: 210px;
    text-align: center;
    color: var(--text-light);
    font-size: 17px;
    font-weight: 400;
  }
  .services .dot {
    color: var(--brand-orange);
    margin: 0 6px;
  }
  .card-back .brand {
    right: 48px;
    top: 58px;
  }
  .card-back .brand-name { font-size: 26px; }
  .back-rule {
    position: absolute;
    right: 48px;
    top: 106px;
    width: 300px;
    height: 1px;
    background: var(--rule-grey);
  }
  .contact {
    position: absolute;
    left: 56px;
    bottom: 44px;
    color: var(--text-light);
  }
  .contact-name {
    color: var(--brand-orange);
    font-weight: 700;
    font-size: 20px;
  }
  .contact-role {
    font-size: 16px;
    margin-bottom: 14px;
  }
  .contact-line {
    display: flex;
    align-items: center;
    gap: 10px;
    font-size: 16px;
    margin-top: 6px;
  }
  .contact-line svg { width: 18px; height: 18px; flex: none; }
</style>
</head>
<body>
<main class="canvas">

  <section class="card card-front">
    <svg class="card-frame" viewBox="0 0 640 366" preserveAspectRatio="none">
      <rect width="640" height="366" fill="var(--brand-orange)"/>
      <rect x="12" y="12" width="616" height="342" fill="var(--card-dark)"/>
      <polygon points="580,0 640,0 640,60 628,60 580,12" fill="var(--card-dark)"/>
      <polygon points="0,306 12,306 60,354 60,366 0,366" fill="var(--card-dark)"/>
    </svg>
    <div class="brand">
      <span class="brand-square"></span>
      <span class="brand-name">Harbour Pine Supply</span>
    </div>
    <div class="front-rule"></div>
    <p class="services">Generators<span class="dot">•</span>Lighting Towers<span class="dot">•</span>De-watering Pumps<span class="dot">•</span>Compressors</p>
  </section>

  <section class="card card-back">
    <svg class="card-frame" viewBox="0 0 640 366" preserveAspectRatio="none">
      <rect width="640" height="366" fill="var(--brand-orange)"/>
      <rect x="12" y="12" width="616" height="342" fill="var(--card-dark)"/>
      <polygon points="580,0 640,0 640,60 628,60 580,12" fill="var(--card-dark)"/>
      <polygon points="0,306 12,306 60,354 60,366 0,366" fill="var(--card-dark)"/>
    </svg>
    <div class="brand">
      <span class="brand-square"></span>
      <span class="brand-name">Harbour Pine Supply</span>
    </div>
    <div class="back-rule"></div>
    <div class="contact">
      <p class="contact-name">Owen Pritchard</p>
      <p class="contact-role">Director</p>
      <p class="contact-line">
        <svg viewBox="0 0 24 24" aria-hidden="true"><path fill="var(--text-light)" d="M6.6 10.8a15.1 15.1 0 0 0 6.6 6.6l2.2-2.2c.3-.3.7-.4 1-.2 1.1.4 2.3.6 3.6.6.6 0 1 .4 1 1V20c0 .6-.4 1-1 1A17 17 0 0 1 3 4c0-.6.4-1 1-1h3.5c.6 0 1 .4 1 1 0 1.3.2 2.5.6 3.6.1.3 0 .7-.2 1z"/></svg>
        0461527390
      </p>
      <p class="contact-line">
        <svg viewBox="0 0 24 24" aria-hidden="true"><rect x="2" y="5" width="20" height="14" rx="1" fill="var(--text-light)"/><path d="M2 6l10 7 10-7" fill="none" stroke="var(--card-dark)" stroke-width="1.6"/></svg>
        harbourpinesupply@postvale.net
      </p>
    </div>
  </section>

</main>
</body>
</html>
```